ONE PAGE WEB DESIGN NEEDED for Finance Company

We need a web design (ONE PAGE DESIGN ONLY) for a new finance website called Brightwell Lending. Brightwell Lending helps customers get the right loan, whether its a home loan, investment loan, business loan etc.

You are required to come up with just the homepage design. Professionalism and quality is the key factors in the successful design.

Here are a few design questions to help you out:

-
What information should be used on the page?
Ive provided a document which outlines all the information needed to put on homepage (attached to the brief - called brightwell_page_info). Also see the Must Have section below on this brief.

-
What links should appear in the navigation/footer?:
The navigation should provide links to the following pages (NOTE: services link has subcategories):
1 Homepage
2 Services
- Home loans
- Investment loans
- Refinancing loans
- Business loans
3 About Us
4 FAQ
5 Contact Us

-
What colors should be used in the design?
Our company colors - Cyan: #2EADE3, Blue: #004B70, White. Feel free to submit designs with slight variations if you feel it improves the design.

-
What should the layout of the page be?
This is up to you to come up with - we are open to different layouts for the page design (as long as they capture the information effectively and making it easy to understand).

Target Market(s)

Potential Home owners, Families and Business Owners

Industry/Entity Type

Business

Requirements
Must have
• - Must contain our logo (attached as PNG and Illustrator file)
- Winning designer must supply a Photoshop file (PSD) that will allow us.
Nice to have
• - Should include photos/images of families, professional groups, tradespeople etc (you can use stock photos from PixQuarry and I will purchase them once you are selected as the winning design)
- Link to a loan calculator somewhere on front page with a button 'Find out how much you could borrow' (or maybe even try adding a loan calculator to the homepage if you think this would look good)
- Page should have a main headline "Finding the right loan for you" or "Brightwell Lending finds the right loan for our customers."
- Must include Accreditation logos somewhere on the homepage (will try and supply these soon)
Should not have
• - Poor quality designs will not be considered
- Do not use clipart

```html
<!DOCTYPE html>
<html lang="en">
<head>
<meta charset="utf-8">
<title>Brightwell Lending</title>
<link rel="stylesheet" href="https://fonts.googleapis.com/css2?family=Arimo:wght@400;700&display=swap">
<style>
:root{
  --cyan:#1ea6e0;
  --cyan-bright:#0fb0ec;
  --blue:#004b70;
  --blue-nav:#0a5b86;
  --text:#4a4a4a;
  --muted:#666;
  --line:#e3e3e3;
  --band:#f6f6f6;
  --footer:#333;
  --footer-text:#bdbdbd;
  --white:#fff;
}
*{box-sizing:border-box;margin:0;padding:0}
html,body{width:1087px;height:1200px;overflow:hidden}
body{position:relative;background:var(--white);font-family:"Arimo",Arial,sans-serif;color:var(--text)}
.topbar{position:absolute;left:0;top:0;width:1087px;height:10px;background:var(--blue)}
.header{position:absolute;left:0;top:10px;width:1087px;height:168px;background:linear-gradient(#eeeeee,#f9f9f9 60%,#f3f3f3)}
.brand{position:absolute;left:80px;top:108px;display:flex;align-items:center;gap:10px}
.brand-dot{width:30px;height:30px;border-radius:50%;background:var(--cyan)}
.brand-name{font-size:29px;font-weight:700;color:var(--cyan);letter-spacing:-.5px}
.search{position:absolute;left:852px;top:46px;width:154px;height:28px;border:1px solid #cfcfcf;border-radius:3px;background:#fff;font-size:11px;font-style:italic;color:#aaa;padding:8px 10px}
.search svg{position:absolute;right:8px;top:8px}
.nav{position:absolute;left:524px;top:97px;width:482px;height:45px;display:flex;background:linear-gradient(#146a98,var(--blue));border-radius:5px;overflow:visible}
.nav a{display:flex;align-items:center;justify-content:center;color:#fff;font-size:13.5px;text-decoration:none;border-right:1px solid #0b4666;border-left:1px solid #2a7aa6}
.nav a:first-child{border-left:0;border-radius:5px 0 0 5px}
.nav a:last-child{border-right:0}
.nav .active{background:var(--cyan-bright)}
.dropdown{position:absolute;left:609px;top:142px;width:135px;height:115px;background:var(--cyan-bright);padding:11px 0 0 18px;list-style:none;z-index:2}
.dropdown li{color:#fff;font-size:11.5px;line-height:22.7px}
.dropdown li::before{content:"•";margin-right:8px}
.hero{position:absolute;left:80px;top:180px;width:926px;height:287px;background:var(--blue);padding:6px;box-shadow:0 8px 10px -6px rgba(0,0,0,.35)}
.hero-photo{width:100%;height:100%;background:linear-gradient(100deg,#cfe2f2 0%,#5d94d2 35%,#1f4f9a 60%,#9fc2e6 80%,#1c3f7c 100%)}
.hero-caption{position:absolute;left:6px;bottom:5px;width:375px;height:44px;background:rgba(20,30,40,.8);color:#fff;font-size:17px;padding:13px 28px}
.hero-arrows{position:absolute;right:14px;top:15px}
.welcome{position:absolute;left:80px;top:505px;width:703px}
.welcome h1{font-size:20px;font-weight:400;color:var(--blue);margin-bottom:14px}
.welcome p{font-size:12.4px;line-height:21px;margin-bottom:7px}
.borrow{position:absolute;left:808px;top:529px;width:197px;height:124px;border:2px solid #d8d8d8;border-radius:5px;background:linear-gradient(#f2f2f2,#e4e4e4);padding:8px 16px}
.borrow h2{font-size:20px;font-weight:400;color:var(--blue);line-height:26px}
.borrow-btn{position:absolute;left:16px;top:71px;width:171px;height:36px;background:#fff;border-radius:5px;display:flex;align-items:center;gap:14px;padding-left:4px;font-size:12.5px;color:#333}
.borrow-btn .cash{width:78px;height:26px;background:linear-gradient(90deg,#b8c9a8,#6f8a5d);border-radius:3px}
.borrow-btn span{text-decoration:underline}
.band{position:absolute;left:0;top:680px;width:1087px;height:200px;background:var(--band)}
.cards{position:absolute;left:81px;top:707px;display:flex;gap:8px}
.card{width:225px;height:166px;background:#fff;border:1px solid #ececec;box-shadow:inset 0 0 12px rgba(0,0,0,.05)}
.card h3{display:flex;align-items:center;gap:14px;height:46px;padding-left:14px;border-bottom:1px solid var(--line);font-size:17px;font-weight:400;color:var(--cyan)}
.card ul{list-style:none;padding:10px 0 0 22px}
.card li{position:relative;font-size:13.2px;color:#555;line-height:19px;margin-bottom:7.5px;padding-left:20px;padding-right:10px}
.card li::before{content:"";position:absolute;left:0;top:5px;border-left:5px solid #999;border-top:4px solid transparent;border-bottom:4px solid transparent}
.lenders{position:absolute;left:80px;top:900px;width:926px;font-size:12.4px;line-height:21px}
.contact-line{position:absolute;left:80px;top:949px;font-size:16.5px;color:var(--blue)}
.divider{position:absolute;left:120px;top:1002px;width:846px;height:1px;background:linear-gradient(90deg,transparent,#d5d5d5 20%,#d5d5d5 80%,transparent)}
.partners{position:absolute;left:100px;top:1035px;width:880px;display:flex;justify-content:space-between;align-items:center}
.partner{height:34px;background:#c9c9c9;border-radius:4px}
.footer{position:absolute;left:0;top:1109px;width:1087px;height:91px;background:var(--footer);color:var(--footer-text);font-size:11.8px}
.footer-nav{position:absolute;left:80px;top:17px}
.footer-nav span{margin:0 9px;color:#888}
.copyright{position:absolute;left:80px;top:47px}
.social{position:absolute;left:887px;top:28px;display:flex;gap:9px}
.social i{width:23px;height:23px;border-radius:50%;background:#6a6a6a;display:flex;align-items:center;justify-content:center}
</style>
</head>
<body>
<div class="topbar"></div>
<header class="header">
  <div class="brand"><div class="brand-dot"></div><div class="brand-name">Brightwell Lending</div></div>
  <div class="search">Search
    <svg width="11" height="11" viewBox="0 0 11 11"><circle cx="4.5" cy="4.5" r="3.5" fill="none" stroke="#bbb" stroke-width="1.4"/><line x1="7" y1="7" x2="10" y2="10" stroke="#bbb" stroke-width="1.6"/></svg>
  </div>
</header>
<nav class="nav">
  <a href="#" style="width:85px">Home</a>
  <a href="#" class="active" style="width:102px">Services</a>
  <a href="#" style="width:102px">About us</a>
  <a href="#" style="width:80px">FAQ</a>
  <a href="#" style="width:113px">Contact us</a>
</nav>
<ul class="dropdown">
  <li>Home loans</li><li>Investment loans</li><li>Refinancing loans</li><li>Business loans</li>
</ul>
<section class="hero">
  <div class="hero-photo" role="img" aria-label="Photo looking up at glass office towers against a blue sky"></div>
  <div class="hero-caption">Finding the right loan for you
    <svg class="hero-arrows" width="30" height="14" viewBox="0 0 30 14"><polyline points="8,1 2,7 8,13" fill="none" stroke="#fff" stroke-width="2.5"/><polyline points="20,1 26,7 20,13" fill="none" stroke="#fff" stroke-width="2.5"/></svg>
  </div>
</section>
<section class="welcome">
  <h1>Welcome to our site</h1>
  <p>At Brightwell Lending we work hard to find the right loan for our customers. We do that because we are backed by sound industry knowledge, professional experience and a great customer service approach.</p>
  <p>Brightwell Lending guarantees that we will always tailor the best solution for your individual lending needs.</p>
  <p>We can do that because we have access to a wide variety of lending options from major banks to non-bank lenders and we are committed to finding the right lending product for you.</p>
</section>
<aside class="borrow">
  <h2>Find how much you could borrow</h2>
  <div class="borrow-btn"><div class="cash" role="img" aria-label="Banknotes and a calculator"></div><span>Click here</span></div>
</aside>
<div class="band"></div>
<section class="cards">
  <div class="card"><h3><svg width="24" height="22" viewBox="0 0 24 22"><polygon points="12,2 22,11 2,11" fill="#8a8a8a"/><rect x="5" y="10" width="14" height="10" fill="#ddd" stroke="#999"/><rect x="10" y="13" width="4" height="4" fill="#1e7fc2"/></svg>Home Loan</h3>
    <ul><li>Home buyers</li><li>First home buyers</li><li>Over 20 lenders</li></ul></div>
  <div class="card"><h3><svg width="24" height="24" viewBox="0 0 24 24"><text x="12" y="20" text-anchor="middle" font-family="Arimo,Arial,sans-serif" font-weight="700" font-size="22" fill="#3aa53a">$</text></svg>Investment Loan</h3>
    <ul><li>Property investment loans</li><li>Interest only loans</li></ul></div>
  <div class="card"><h3><svg width="24" height="24" viewBox="0 0 24 24"><rect x="3" y="3" width="18" height="18" fill="#fafafa" stroke="#bbb"/><polyline points="5,17 10,11 14,14 19,6" fill="none" stroke="#e04a3a" stroke-width="2"/></svg>Refinancing</h3>
    <ul><li>Refinancing for the best rate</li><li>Upsizing or downsizing</li><li>Change from a variable to a fixed rate</li></ul></div>
  <div class="card"><h3><svg width="26" height="22" viewBox="0 0 26 22"><rect x="9" y="2" width="8" height="5" fill="none" stroke="#7a3a1a" stroke-width="2"/><rect x="1" y="6" width="24" height="15" rx="2" fill="#c4551f"/><line x1="1" y1="12" x2="25" y2="12" stroke="#8a3510" stroke-width="1.5"/></svg>Business Loan</h3>
    <ul><li>Long term</li><li>Short term</li><li>Equipment and Leasing</li></ul></div>
</section>
<p class="lenders">There are many different loan products in the marketplace. Brightwell Lending has access to a wide panel of lenders which means we can access bank and non-bank lenders that meet the individual needs of our customers.</p>
<p class="contact-line">Contact Brightwell Lending today on: 1800 555 210 to find out more.</p>
<div class="divider"></div>
<div class="partners" aria-label="Accreditation partners">
  <div class="partner" style="width:64px;border-radius:50%"></div>
  <div class="partner" style="width:90px"></div>
  <div class="partner" style="width:50px"></div>
  <div class="partner" style="width:86px;height:20px"></div>
  <div class="partner" style="width:94px;height:12px"></div>
  <div class="partner" style="width:80px;height:22px"></div>
  <div class="partner" style="width:44px"></div>
</div>
<footer class="footer">
  <div class="footer-nav">Home<span>|</span>Services<span>|</span>About us<span>|</span>FAQ<span>|</span>Contact us</div>
  <div class="copyright">Copyright &copy; 2012 &nbsp;www.brightwelllending.com &nbsp; All rights reserved.</div>
  <div class="social">
    <i></i><i></i><i></i>
    <i><svg width="13" height="10" viewBox="0 0 13 10"><rect x=".5" y=".5" width="12" height="9" fill="none" stroke="#ddd"/><polyline points=".5,.5 6.5,5.5 12.5,.5" fill="none" stroke="#ddd"/></svg></i>
  </div>
</footer>
</body>
</html>
```